Tavon Web Design Project

We need a web design for a research project in Tuscany, Italy regarding trash collection in industrial sites using innovative garbage bin. Those innovative bin can communicate in wireless way their status and reserve their emptying to the operating trash company. To the other side the project give to trash company a logistic system in order to plan emptying operations aiming to optimize vehicles routing.

At this link you can find the logo of the project, previously realized and not changeble.

http://www.progetto-tavon.example/tavon/resources/logo_web.png

Industry/Entity Type

It Company

```html
<!DOCTYPE html>
<html lang="it">
<head>
<meta charset="utf-8">
<title>Tavon – il progetto</title>
<link rel="stylesheet" href="https://fonts.googleapis.com/css2?family=Open+Sans:wght@400;600;700&display=swap">
<style>
  :root {
    --page-bg: #ebebeb;
    --paper: #ffffff;
    --accent: #99cc22;
    --logo-ink: #222222;
    --nav-ink: #8a8a8a;
    --nav-rule: #c9c9c9;
    --body-ink: #6b6b6b;
  }
  * { box-sizing: border-box; margin: 0; padding: 0; }
  html, body {
    width: 1200px; height: 675px; overflow: hidden;
    background: var(--page-bg);
  }
  .page {
    position: absolute; left: 170px; top: 0;
    width: 843px; height: 675px; overflow: hidden;
    background: var(--paper);
    border-top: 3px solid var(--accent);
    box-shadow: 0 0 3px rgba(0,0,0,0.12);
  }
  .brand {
    position: absolute; left: 36px; top: 50px;
    display: flex; align-items: center; gap: 8px;
  }
  .brand-mark {
    width: 16px; height: 16px; border-radius: 50%;
    background: var(--accent);
  }
  .brand-name {
    font-family: "Open Sans", sans-serif; font-weight: 700;
    font-size: 34px; line-height: 40px; color: var(--logo-ink); letter-spacing: 0.5px;
  }
  .main-nav {
    position: absolute; left: 554px; top: 58px;
    display: grid; grid-template-columns: 109px 109px;
    column-gap: 37px; row-gap: 10px;
    list-style: none;
  }
  .main-nav li {
    font-family: "Open Sans", sans-serif; font-size: 10px;
    color: var(--nav-ink); border-bottom: 1px solid var(--nav-rule);
    line-height: 13px;
  }
  .main-nav li.is-current { font-weight: 700; color: #777; }
  .feature-tiles {
    position: absolute; left: 36px; top: 161px;
    display: flex; gap: 4px;
  }
  .tile {
    position: relative; width: 255px; height: 176px; overflow: hidden;
  }
  .tile-photo { position: absolute; inset: 0; }
  .tile--project .tile-photo { background: linear-gradient(100deg, #5f8a1e 0%, #7ea730 45%, #a3cc4c 100%); }
  .tile--partners .tile-photo { background: radial-gradient(circle at 50% 50%, #d6d6d6 0%, #9a9a9a 45%, #5c5c5c 100%); }
  .tile--docs .tile-photo { background: linear-gradient(90deg, #ffffff 0%, #e8e8e8 45%, #8d8d8d 80%, #cfcfcf 100%); }
  .tile-rule {
    position: absolute; left: 0; right: 0; top: 91px; height: 2px;
    background: var(--accent);
  }
  .tile-label {
    position: absolute; left: 0; right: 0; top: 68px; text-align: center;
    font-family: "Open Sans", sans-serif; font-weight: 600; font-size: 17px;
    line-height: 22px;
    color: #ffffff; text-shadow: 0 1px 2px rgba(0,0,0,0.55);
  }
  .divider-shadow {
    position: absolute; left: 0; right: 0; top: 372px; height: 12px;
    background: linear-gradient(to bottom, rgba(0,0,0,0.05), rgba(0,0,0,0));
  }
  .section-title {
    position: absolute; left: 0; top: 420px; width: 229px; height: 34px;
    background: var(--accent); color: #ffffff;
    font-family: "Open Sans", sans-serif; font-size: 19px; font-weight: 400;
    text-align: right; padding-right: 12px; line-height: 34px;
  }
  .intro-text {
    position: absolute; left: 295px; top: 421px; width: 498px;
    height: 251px; overflow: hidden;
    font-family: Arial, Helvetica, sans-serif; font-size: 12.4px;
    line-height: 20.2px; color: var(--body-ink);
  }
</style>
</head>
<body>
<div class="page">
  <div class="brand">
    <span class="brand-mark"></span>
    <span class="brand-name">Tavon</span>
  </div>

  <ul class="main-nav">
    <li class="is-current">il progetto</li>
    <li>i partners</li>
    <li>la documentazione</li>
    <li>links</li>
    <li>appuntamenti</li>
    <li>area protetta</li>
  </ul>

  <div class="feature-tiles">
    <div class="tile tile--project">
      <div class="tile-photo" role="img" aria-label="Foto in tinta verde di un cassonetto industriale accanto a un muro"></div>
      <div class="tile-rule"></div>
      <div class="tile-label">il progetto</div>
    </div>
    <div class="tile tile--partners">
      <div class="tile-photo" role="img" aria-label="Foto in bianco e nero di mani che si stringono i polsi in cerchio sull'erba"></div>
      <div class="tile-rule"></div>
      <div class="tile-label">i partners</div>
    </div>
    <div class="tile tile--docs">
      <div class="tile-photo" role="img" aria-label="Foto in bianco e nero di una pila di fascicoli di documenti"></div>
      <div class="tile-rule"></div>
      <div class="tile-label">la documentazione</div>
    </div>
  </div>

  <div class="divider-shadow"></div>

  <h2 class="section-title">Introduzione</h2>

  <p class="intro-text">Il progetto ha come obiettivo la progettazione e sviluppo sperimentale di una piattaforma di servizi di infomobilità e tracciamento per la raccolta e trasporto dei rifiuti speciali. La piattaforma è distinta in due componenti principali: una componente periferica, costituita da tecnologie di identificazione e sensoristica per l'acquisizione in tempo reale di dati utili per il controllo e monitoraggio dei rifiuti speciali e dei veicoli addetti al trasporto, ed un Centro Servizi che ospita la logica applicativa per l'integrazione dei dati acquisiti e per i servizi applicativi di gestione delle flotte e tracciamento dei rifiuti nelle fasi di raccolta e trasporto. Un'architettura di questo genere consente l'ottimizzazione della raccolta e del trasporto fornendo una base dati completa che traccia ogni carico dal punto di partenza al punto di arrivo; in questo modo, il processo risulta interamente automatizzato, poiché consente sia di identificare - qualitativamente e quantitativamente - il carico raccolto e trasportato, sia di eliminare i possibili errori operativi che possono insorgere lungo i percorsi dei mezzi addetti alla raccolta (minimizzando la frequenza dei giri di raccolta), sia di ridurre i costi complessivi del servizio.</p>
</div>
</body>
</html>
```